Power Point for a new training package

I am a new business and about to offer my first teaching day. I have all the content, have a logo etc. but need to translate this into a slick bespoke Power Point presentation,

Target Market(s)

Senior people in healthcare sector, UK

Industry/Entity Type

Healthcare

Requirements
Must have
• Sense of originality, use of my logo and associated colour scheme, stylish but simple

```html
<!DOCTYPE html>
<html lang="en">
<head>
<meta charset="utf-8">
<title>Controlled Drug Accountable Officers Mastery – Slide Deck</title>
<link href="https://fonts.googleapis.com/css2?family=Montserrat:wght@400;500;600;700;800&family=Open+Sans:wght@400;600;700&display=swap" rel="stylesheet">
<style>
:root{
  --teal:#1fb3aa;
  --teal-bright:#3fd0c6;
  --teal-deep:#14958d;
  --ink:#1d2626;
  --grey-text:#4a5353;
  --stage:#e4e6e8;
  --paper:#ffffff;
  --rule:#1fb3aa;
}
*{margin:0;padding:0;box-sizing:border-box}
html,body{width:1200px;height:954px;overflow:hidden;background:var(--stage)}
body{position:relative;font-family:'Open Sans',sans-serif;color:var(--ink)}
.slide{position:absolute;width:357px;height:201px;background:var(--paper);overflow:hidden;box-shadow:0 2px 5px rgba(0,0,0,.18)}
.col-1{left:42px}.col-2{left:419px}.col-3{left:796px}
.row-1{top:43px}.row-2{top:262px}.row-3{top:480px}.row-4{top:700px}
.abs{position:absolute}

.slide-title{position:absolute;left:14px;top:7px;font:700 11.5px/1.2 'Montserrat',sans-serif;color:var(--ink)}
.title-rule{position:absolute;left:14px;top:25px;width:42px;height:3px}
.brand-tag{position:absolute;right:8px;top:8px;display:flex;align-items:center;gap:2px}
.brand-tag .dot{width:10px;height:10px;border:1px solid var(--teal);border-radius:50%}
.brand-tag .name{font:600 3.6px/1.1 'Montserrat',sans-serif;color:var(--ink)}
.slide-foot{position:absolute;left:7px;right:8px;bottom:7px;height:8px}
.slide-foot .dot{position:absolute;left:0;top:0;width:7px;height:7px;border:.7px solid var(--teal);border-radius:50%}
.slide-foot .legal{position:absolute;left:11px;top:2px;font:600 2.6px 'Montserrat',sans-serif;color:var(--ink)}
.slide-foot .line{position:absolute;left:11px;right:6px;top:6px;height:.5px;background:var(--rule)}
.slide-foot .page{position:absolute;right:0;top:2px;font:600 3.6px 'Montserrat',sans-serif}
.photo{position:absolute}

.cover{background:linear-gradient(120deg,#4ad6cc,#33c7bd 60%,#2fc1b7)}
.cover .ring{left:38px;top:50px;width:102px;height:102px;border:4px solid rgba(150,245,238,.6);border-radius:50%}
.cover .brand{left:147px;top:76px;font:600 16.5px/1 'Montserrat',sans-serif;color:var(--ink)}
.cover .brand span{display:block;font-weight:400;color:#22403f}
.cover .band{left:135px;top:120px;right:0;height:15px;background:#fff;border-radius:8px 0 0 8px}
.cover .band p{position:absolute;left:10px;top:2px;font:700 8.6px 'Open Sans',sans-serif;color:var(--teal);letter-spacing:-.1px}
.cover .team{left:145px;top:139px;font:400 5.9px 'Open Sans',sans-serif;color:#0f3a38}

.title-slide .left{left:0;top:0;width:150px;height:201px;background:linear-gradient(135deg,#fafafa,#ededed)}
.title-slide .brand-block{left:0;width:150px;top:14px;text-align:center}
.title-slide .brand-block .dot{width:26px;height:26px;border:2px solid var(--teal);border-radius:50%;margin:0 auto 5px}
.title-slide .brand-block p{font:500 8.4px/1 'Montserrat',sans-serif}
.title-slide .brand-block p span{display:block;font-weight:400}
.title-slide .kicker{left:18px;top:83px;font:400 8px 'Montserrat',sans-serif;color:var(--teal)}
.title-slide h1{position:absolute;left:18px;top:92px;font:800 15.5px/1 'Montserrat',sans-serif;color:var(--ink)}
.title-slide h1 em{font-style:normal;color:var(--teal);display:block}
.title-slide .team{left:18px;top:155px;font:400 6.1px/1.8 'Open Sans',sans-serif}
.title-slide .pager{left:108px;top:184px;display:flex;gap:4px}
.title-slide .pager i{width:3.5px;height:3.5px;border-radius:50%;background:var(--ink)}
.title-slide .pager i.on{background:var(--teal)}
.title-slide .site{left:150px;top:164px;right:0;bottom:0;background:var(--teal);color:#fff;font:400 6.6px 'Open Sans',sans-serif;letter-spacing:2.4px;text-align:center;padding-top:16px}

.objectives h2{position:absolute;right:222px;top:87px;text-align:right;font:600 12px/1.1 'Montserrat',sans-serif;white-space:nowrap}
.objectives h2 em{font-style:normal;color:var(--teal);font-weight:700}
.bullets{list-style:none}
.bullets li{position:relative;padding-left:8px}
.bullets li::before{content:"";position:absolute;left:0;top:.55em;width:2.4px;height:2.4px;border-radius:50%;background:var(--teal)}
.objectives ul{position:absolute;left:147px;top:53px;font:400 6.9px/1.25 'Open Sans',sans-serif;width:200px}
.objectives li{margin-bottom:6px}

.why .band{left:32px;top:99px;width:290px;height:63px;background:var(--teal)}
.why .card{position:absolute;top:65px;width:77px;height:80px;background:#fff;border:1.3px solid var(--teal);border-radius:7px;box-shadow:2px 3px 4px rgba(0,0,0,.18);text-align:center;font:400 6.7px/1.33 'Open Sans',sans-serif;padding:21px 8px 0}
.why .badge{position:absolute;left:50%;top:-14px;width:28px;height:28px;margin-left:-14px;border:1.3px solid var(--teal);border-radius:50%;background:#fff;display:flex;align-items:center;justify-content:center}

.deaths svg text{font-family:'Open Sans',sans-serif}

.legal-box{left:17px;top:47px;width:143px;height:114px;background:var(--teal);color:#fff;padding:6px 6px 0 7px}
.legal-box ul{list-style:none;font:400 5.5px/1.35 'Open Sans',sans-serif}
.legal-box li{margin-bottom:3.2px}
.legal-box li::before{content:"• "}
.legal-box li.sub{padding-left:3px}
.legal-box li.sub::before{content:"› "}

.laws .band{left:0;top:35px;width:357px;height:139px;background:linear-gradient(90deg,#7d8e9b 0%,#8fa4ae 30%,#5fb3b0 52%,var(--teal) 62%)}
.laws .copy{left:180px;top:41px;width:172px;color:#fff}
.laws h3{font:700 7.8px 'Open Sans',sans-serif;margin-bottom:4px}
.laws .lead{font:400 6.7px/1.2 'Open Sans',sans-serif;padding-left:9px;position:relative;margin-bottom:3px}
.laws .lead::before{content:"➢";position:absolute;left:0;font-size:5.5px;top:1px}
.laws ul{list-style:none;font:400 5.6px/1.75 'Open Sans',sans-serif;padding-left:30px;margin-bottom:5px}
.laws ul li::before{content:"• "}

.issues .lbl{position:absolute;font:400 5.5px/1.2 'Open Sans',sans-serif}
.issues .lbl.l{text-align:right;right:272px}
.issues .lbl.r{left:259px}

.consider .tile{position:absolute;width:27px;height:27px;display:flex;align-items:center;justify-content:center}
.consider .tile.t{background:var(--teal);border:1px solid #8fe0da}
.consider .tile.k{background:var(--ink)}
.consider .cap{position:absolute;font:700 4.6px/1.3 'Montserrat',sans-serif;text-transform:uppercase;width:62px}

.invest .node{position:absolute;width:29px;height:29px;border-radius:50%;background:var(--teal);border:2px solid #fff;box-shadow:0 0 0 .8px #c9eeeb;display:flex;align-items:center;justify-content:center}
.invest .cap{position:absolute;font:700 5.7px/1.35 'Open Sans',sans-serif;text-transform:uppercase}
.invest .who{left:130px;top:112px;width:102px;text-align:center;font:800 10.5px/1.1 'Montserrat',sans-serif}

.speak ul{position:absolute;left:155px;top:56px;width:190px;font:400 7px/1.3 'Open Sans',sans-serif}
.speak li{margin-bottom:7px}

.thanks .ring{left:-40px;top:20px;width:200px;height:200px;border:14px solid #eef0f1;border-radius:50%}
.thanks .brand{left:188px;top:43px;font:600 13.5px/1 'Montserrat',sans-serif}
.thanks .brand span{display:block;font-weight:400}
.thanks h2{position:absolute;left:188px;top:82px;font:800 21px 'Montserrat',sans-serif}
.thanks .contact{position:absolute;left:188px;display:flex;align-items:center;gap:4px;font:400 5.2px/1.3 'Open Sans',sans-serif;color:var(--grey-text)}
.thanks .contact .bar{width:.6px;height:9px;background:var(--ink)}
.thanks .strip{left:0;bottom:0;width:357px;height:10px}
</style>
</head>
<body>

<section class="slide col-1 row-1 cover">
  <div class="abs ring"></div>
  <div class="abs brand">Kestrel Ward<span>Consulting</span></div>
  <div class="abs band"><p>Controlled Drug Accountable Officers MASTERY</p></div>
  <div class="abs team">Tom Harland &nbsp;| &nbsp;Keiran Ward &nbsp;| &nbsp;Wendy Ashby</div>
</section>

<section class="slide col-2 row-1 title-slide">
  <div class="abs left"></div>
  <div class="abs brand-block"><div class="dot"></div><p>Kestrel Ward<span>Consulting</span></p></div>
  <div class="abs kicker">Controlled Drug</div>
  <h1>Accountable<br>Officers<em>MASTERY</em></h1>
  <div class="abs team">Tom Harland<br>Keiran Ward<br>Wendy Ashby</div>
  <div class="abs pager"><i></i><i class="on"></i><i></i></div>
  <div class="photo" role="img" aria-label="Portrait photograph of the lead trainer in a navy suit" style="left:150px;top:0;width:207px;height:164px;background:linear-gradient(160deg,#e8eaea 0%,#c9cfd2 55%,#39435c 100%)"></div>
  <div class="abs site">kestrelwardconsulting.com</div>
</section>

<section class="slide col-3 row-1 objectives">
  <div class="brand-tag"><span class="dot"></span><span class="name">Kestrel Ward<br>Consulting</span></div>
  <h2>Objectives For<br>This <em>Presentation</em></h2>
  <ul class="bullets">
    <li>Reflect on why we have controls on drugs</li>
    <li>Do controls work?</li>
    <li>The difference between the Misuse of Drugs Act and the Regulations</li>
    <li>The need to have controls for healthcare professionals</li>
    <li>Controlled Drug Accountable Officers</li>
    <li>Local Intelligence Networks</li>
  </ul>
  <div class="slide-foot"><span class="dot"></span><span class="legal">©2023. Kestrel Ward Consulting Ltd</span><span class="line"></span><span class="page">2</span></div>
</section>

<section class="slide col-1 row-2 why">
  <h2 class="slide-title">Why Are Some Drugs Controlled?</h2>
  <svg class="title-rule" viewBox="0 0 42 3"><circle cx="1.2" cy="1.5" r="1.1" fill="#1fb3aa"/><circle cx="4.2" cy="1.5" r="1.1" fill="#1fb3aa"/><circle cx="7.2" cy="1.5" r="1.1" fill="#1fb3aa"/><rect x="9.5" y=".6" width="32" height="1.8" fill="#1fb3aa"/></svg>
  <div class="brand-tag"><span class="dot"></span><span class="name">Kestrel Ward<br>Consulting</span></div>
  <div class="abs band"></div>
  <div class="card" style="left:48px">
    <span class="badge"><svg width="14" height="13" viewBox="0 0 14 13"><path d="M7 1 13 12H1Z" fill="none" stroke="#1fb3aa" stroke-width="1.2" stroke-linejoin="round"/><path d="M7 5v3.5M7 10v.5" stroke="#1fb3aa" stroke-width="1.2"/></svg></span>
    All medicines can be dangerous, and we need to be careful with all of them
  </div>
  <div class="card" style="left:139px">
    <span class="badge"><svg width="14" height="14" viewBox="0 0 14 14"><rect x="2" y="3" width="4" height="10" rx="1" fill="none" stroke="#1fb3aa"/><path d="M4 1v2M3 6h2" stroke="#1fb3aa"/><rect x="8" y="6" width="4" height="7" rx="1" fill="none" stroke="#1fb3aa"/></svg></span>
    Insulin can be extremely harmful, but it isn't addictive
  </div>
  <div class="card" style="left:229px">
    <span class="badge"><svg width="14" height="14" viewBox="0 0 14 14"><path d="M2 6h8v3a4 4 0 0 1-8 0Z" fill="#1fb3aa"/><path d="M10 7h1.5a1.5 1.5 0 0 1 0 3H10" fill="none" stroke="#1fb3aa"/><path d="M5 2c0 1.5 1 1.5 1 3M8 2c0 1.5 1 1.5 1 3" stroke="#1fb3aa" fill="none" stroke-width=".8"/></svg></span>
    Caffeine is addictive but it doesn't cause much harm
  </div>
  <div class="slide-foot"><span class="dot"></span><span class="legal">©2023. Kestrel Ward Consulting Ltd</span><span class="line"></span><span class="page">3</span></div>
</section>

<section class="slide col-2 row-2 deaths">
  <h2 class="slide-title">Drug related deaths</h2>
  <svg class="title-rule" viewBox="0 0 42 3"><circle cx="1.2" cy="1.5" r="1.1" fill="#1fb3aa"/><circle cx="4.2" cy="1.5" r="1.1" fill="#1fb3aa"/><circle cx="7.2" cy="1.5" r="1.1" fill="#1fb3aa"/><rect x="9.5" y=".6" width="32" height="1.8" fill="#1fb3aa"/></svg>
  <div class="brand-tag"><span class="dot"></span><span class="name">Kestrel Ward<br>Consulting</span></div>
  <svg class="abs" style="left:15px;top:38px" width="172" height="130" viewBox="0 0 172 130">
    <text x="0" y="5" font-size="3.6" font-weight="700">Figure 1: Mortality rates from drug poisoning decreased for males</text>
    <text x="0" y="10" font-size="3.6" font-weight="700">and increased for females in 2022</text>
    <text x="0" y="17" font-size="3.2">Age-standardised mortality rates for deaths related to drug poisoning, by</text>
    <text x="0" y="22" font-size="3.2">sex, England and Wales, registered between 1993 and 2022</text>
    <g font-size="2.6" fill="#555"><line x1="12" y1="27" x2="22" y2="27" stroke="#2c4a7a"/><text x="24" y="28">Persons</text><line x1="44" y1="27" x2="54" y2="27" stroke="#3a8fd0"/><text x="56" y="28">Males</text><line x1="72" y1="27" x2="82" y2="27" stroke="#1b2d5a"/><text x="84" y="28">Females</text></g>
    <g font-size="2.4" fill="#777"><text x="4" y="36">125</text><text x="4" y="54">100</text><text x="4" y="72">75</text><text x="4" y="90">50</text><text x="4" y="108">25</text><text x="4" y="126">0</text></g>
    <g stroke="#e6e6e6" stroke-width=".4"><line x1="12" y1="35" x2="170" y2="35"/><line x1="12" y1="53" x2="170" y2="53"/><line x1="12" y1="71" x2="170" y2="71"/><line x1="12" y1="89" x2="170" y2="89"/><line x1="12" y1="107" x2="170" y2="107"/><line x1="12" y1="125" x2="170" y2="125"/></g>
    <polyline fill="none" stroke="#3a8fd0" stroke-width=".9" points="14,89 25,82 35,80 45,84 55,80 65,82 75,86 85,80 95,82 105,78 115,76 125,66 135,60 145,50 155,42 162,38 168,40"/>
    <polyline fill="none" stroke="#2c4a7a" stroke-width=".9" points="14,96 25,92 35,90 45,93 55,90 65,92 75,94 85,90 95,92 105,89 115,88 125,80 135,76 145,70 155,66 162,64 168,65"/>
    <polyline fill="none" stroke="#1b2d5a" stroke-width=".9" points="14,104 25,102 35,100 45,103 55,101 65,103 75,104 85,101 95,103 105,101 115,101 125,97 135,94 145,92 155,90 162,88 168,87"/>
  </svg>
  <svg class="abs" style="left:196px;top:36px" width="148" height="138" viewBox="0 0 148 138">
    <text x="0" y="4" font-size="3.2" font-weight="700">Figure 6: Drug poisonings involving cocaine continued to increase</text>
    <text x="0" y="8.5" font-size="3.2" font-weight="700">in 2022</text>
    <text x="0" y="14" font-size="2.8">Age-standardised mortality rates for selected substances, by sex, England</text>
    <text x="0" y="18" font-size="2.8">and Wales, deaths registered between 1993 to 2022</text>
    <g font-size="2.4" fill="#555"><circle cx="1.5" cy="22" r=".9" fill="#6b3fa0"/><text x="4" y="23">Female</text><circle cx="16" cy="22" r=".9" fill="#3a8fd0"/><text x="18.5" y="23">Male</text></g>
    <g font-size="2.7" fill="#333">
      <text x="8" y="33">Tramadol</text><text x="44" y="33">Codeine</text><text x="80" y="33">Cocaine</text><text x="116" y="33">Any amphetamine</text>
      <text x="8" y="69">Ecstasy / MDMA</text><text x="44" y="69">Cannabis</text><text x="80" y="69">New psychoactive</text><text x="116" y="69">Benzodiazepine</text>
      <text x="8" y="105">Zopiclone</text><text x="44" y="105">Any antidepressant</text><text x="80" y="105">Any antipsychotic</text><text x="116" y="105">Paracetamol</text>
    </g>
    <g fill="none" stroke-width=".6">
      <polyline stroke="#3a8fd0" points="8,60 16,58 24,56 34,57"/><polyline stroke="#6b3fa0" points="8,61 20,60 34,60"/>
      <polyline stroke="#3a8fd0" points="44,60 56,59 70,57"/><polyline stroke="#6b3fa0" points="44,61 70,60"/>
      <polyline stroke="#3a8fd0" points="80,61 92,60 100,54 106,44"/><polyline stroke="#6b3fa0" points="80,61 106,59"/>
      <polyline stroke="#3a8fd0" points="116,60 128,58 142,57"/><polyline stroke="#6b3fa0" points="116,61 142,60"/>
      <polyline stroke="#3a8fd0" points="8,96 20,95 34,95"/><polyline stroke="#3a8fd0" points="44,96 70,95"/><polyline stroke="#3a8fd0" points="80,96 106,96"/>
      <polyline stroke="#3a8fd0" points="116,96 128,93 142,89"/><polyline stroke="#6b3fa0" points="116,97 142,93"/>
      <polyline stroke="#3a8fd0" points="8,132 34,131"/><polyline stroke="#6b3fa0" points="44,131 56,129 70,130"/><polyline stroke="#6b3fa0" points="80,132 106,131"/><polyline stroke="#6b3fa0" points="116,128 126,127 142,132"/>
    </g>
    <g stroke="#ddd" stroke-width=".4"><line x1="8" y1="62" x2="34" y2="62"/><line x1="44" y1="62" x2="70" y2="62"/><line x1="80" y1="62" x2="106" y2="62"/><line x1="116" y1="62" x2="142" y2="62"/><line x1="8" y1="98" x2="34" y2="98"/><line x1="44" y1="98" x2="70" y2="98"/><line x1="80" y1="98" x2="106" y2="98"/><line x1="116" y1="98" x2="142" y2="98"/><line x1="8" y1="134" x2="34" y2="134"/><line x1="44" y1="134" x2="70" y2="134"/><line x1="80" y1="134" x2="106" y2="134"/><line x1="116" y1="134" x2="142" y2="134"/></g>
  </svg>
  <div class="slide-foot"><span class="dot"></span><span class="legal">©2023. Kestrel Ward Consulting Ltd</span><span class="line"></span><span class="page">4</span></div>
</section>

<section class="slide col-3 row-2">
  <h2 class="slide-title">Heroin And Cocaine Are Legal</h2>
  <svg class="title-rule" viewBox="0 0 42 3"><circle cx="1.2" cy="1.5" r="1.1" fill="#1fb3aa"/><circle cx="4.2" cy="1.5" r="1.1" fill="#1fb3aa"/><circle cx="7.2" cy="1.5" r="1.1" fill="#1fb3aa"/><rect x="9.5" y=".6" width="32" height="1.8" fill="#1fb3aa"/></svg>
  <div class="brand-tag"><span class="dot"></span><span class="name">Kestrel Ward<br>Consulting</span></div>
  <div class="photo" role="img" aria-label="Photograph of a patient receiving anaesthesia through a mask" style="left:126px;top:32px;width:216px;height:144px;background:linear-gradient(120deg,#cfe3ec,#e9eef1 45%,#b7d4df)"></div>
  <div class="abs legal-box">
    <ul>
      <li>In the UK we still use diamorphine in anaesthesia and end of life care</li>
      <li>We use Cocaine in ENT surgery</li>
      <li>The Misuse of Drugs Act makes all CDs illegal, but…</li>
      <li>The Misuse of Drugs Regulations permit their use in very specific circumstances</li>
      <li class="sub">The Act makes morphine a Class A drug</li>
      <li class="sub">The Regulations make morphine a schedule 2 CD (or a schedule 5…)</li>
    </ul>
  </div>
  <div class="slide-foot"><span class="dot"></span><span class="legal">©2023. Kestrel Ward Consulting Ltd</span><span class="line"></span><span class="page">5</span></div>
</section>

<section class="slide col-1 row-3 laws">
  <h2 class="slide-title">Relevant laws</h2>
  <svg class="title-rule" viewBox="0 0 42 3"><circle cx="1.2" cy="1.5" r="1.1" fill="#1fb3aa"/><circle cx="4.2" cy="1.5" r="1.1" fill="#1fb3aa"/><circle cx="7.2" cy="1.5" r="1.1" fill="#1fb3aa"/><rect x="9.5" y=".6" width="32" height="1.8" fill="#1fb3aa"/></svg>
  <div class="brand-tag"><span class="dot"></span><span class="name">Kestrel Ward<br>Consulting</span></div>
  <div class="abs band" role="img" aria-label="Photograph of a judge's gavel resting beside a stethoscope"></div>
  <div class="abs copy">
    <h3>Health Act 2006 Part 3 Sec 18</h3>
    <p class="lead">Duty to co-operate between health bodies &amp; organisations (HEB, Police, CSR, NRB, PRC etc)</p>
    <ul><li>In relation to controlled drugs</li><li>In order to protect the safety of patients</li></ul>
    <p class="lead">Controlled Drugs (supervision of management &amp; use) Regs 2013 Part 3 Sec 14, 15 &amp; 16</p>
    <ul><li>Establishing the LIN</li><li>Co-operation between responsible bodies</li><li>The sharing of information</li></ul>
  </div>
  <div class="slide-foot"><span class="dot"></span><span class="legal">©2023. Kestrel Ward Consulting Ltd</span><span class="line"></span><span class="page">6</span></div>
</section>

<section class="slide col-2 row-3 issues">
  <h2 class="slide-title">Common issues</h2>
  <svg class="title-rule" viewBox="0 0 42 3"><circle cx="1.2" cy="1.5" r="1.1" fill="#1fb3aa"/><circle cx="4.2" cy="1.5" r="1.1" fill="#1fb3aa"/><circle cx="7.2" cy="1.5" r="1.1" fill="#1fb3aa"/><rect x="9.5" y=".6" width="32" height="1.8" fill="#1fb3aa"/></svg>
  <div class="brand-tag"><span class="dot"></span><span class="name">Kestrel Ward<br>Consulting</span></div>
  <svg class="abs" style="left:0;top:0" width="357" height="201" viewBox="0 0 357 201">
    <g stroke="#1d2626" stroke-width=".9" fill="none">
      <path d="M109,57 L118,57 L146,76"/><path d="M109,91 L128,91"/><path d="M109,123 L128,123"/><path d="M109,156 L118,156 L146,136"/>
      <path d="M241,57 L232,57 L204,76"/><path d="M241,91 L222,91"/><path d="M241,123 L222,123"/><path d="M241,156 L232,156 L204,136"/>
    </g>
    <circle cx="175" cy="107" r="37" fill="#fff" stroke="#1d2626" stroke-width="1.4"/>
    <circle cx="175" cy="107" r="33" fill="#1fb3aa"/>
    <circle cx="175" cy="107" r="19" fill="none" stroke="#fff" stroke-width="3" stroke-dasharray="10 3"/>
    <rect x="172.6" y="96" width="4.8" height="14" rx="1.5" fill="#fff"/><circle cx="175" cy="116" r="2.6" fill="#fff"/>
    <g fill="#1fb3aa"><circle cx="103" cy="57" r="6"/><circle cx="103" cy="91" r="6"/><circle cx="103" cy="123" r="6"/><circle cx="103" cy="156" r="6"/><circle cx="247" cy="57" r="6"/><circle cx="247" cy="91" r="6"/><circle cx="247" cy="123" r="6"/><circle cx="247" cy="156" r="6"/></g>
    <g fill="#fff" font-family="Montserrat,sans-serif" font-weight="700" font-size="6.5" text-anchor="middle"><text x="103" y="59.5">1</text><text x="103" y="93.5">2</text><text x="103" y="125.5">3</text><text x="103" y="158.5">4</text><text x="247" y="59.5">8</text><text x="247" y="93.5">7</text><text x="247" y="125.5">6</text><text x="247" y="158.5">5</text></g>
  </svg>
  <p class="lbl l" style="top:50px">CD register<br>cabine /keys</p>
  <p class="lbl l" style="top:84px">Patients own med<br>/TTO's/TTA's</p>
  <p class="lbl l" style="top:114px">Stock Items – Schedule<br>3,4 &amp; 5 (Morphosol<br>Class A)</p>
  <p class="lbl l" style="top:150px">CARRY OUT STOCK<br>CHECKS &nbsp;- all schedules</p>
  <p class="lbl r" style="top:51px">FRAUD – check ALL CD<br>entries/cross reference</p>
  <p class="lbl r" style="top:85px">Offences: Theft, Possession<br>/ Possession with intent to<br>supply a controlled drug</p>
  <p class="lbl r" style="top:118px">Behaviour – Mental<br>Health / Lone worker</p>
  <p class="lbl r" style="top:150px">Wastage – sharps bins<br>WITNESS destruction</p>
  <div class="slide-foot"><span class="dot"></span><span class="legal">©2023. Kestrel Ward Consulting Ltd</span><span class="line"></span><span class="page">7</span></div>
</section>

<section class="slide col-3 row-3 consider">
  <h2 class="slide-title">Things to consider</h2>
  <svg class="title-rule" viewBox="0 0 42 3"><circle cx="1.2" cy="1.5" r="1.1" fill="#1fb3aa"/><circle cx="4.2" cy="1.5" r="1.1" fill="#1fb3aa"/><circle cx="7.2" cy="1.5" r="1.1" fill="#1fb3aa"/><rect x="9.5" y=".6" width="32" height="1.8" fill="#1fb3aa"/></svg>
  <div class="brand-tag"><span class="dot"></span><span class="name">Kestrel Ward<br>Consulting</span></div>

  <div class="tile t" style="left:33px;top:45px"><svg width="14" height="16" viewBox="0 0 14 16"><rect x="1" y="2" width="12" height="13" rx="1" fill="none" stroke="#fff"/><path d="M4 6h6M4 9h6M4 12h4" stroke="#fff" stroke-width=".8"/></svg></div>
  <p class="cap" style="left:67px;top:50px">Compulsory drug testing for all staff</p>
  <div class="tile k" style="left:137px;top:45px"><svg width="14" height="16" viewBox="0 0 14 16"><path d="M2 1h7l3 3v11H2Z" fill="none" stroke="#fff"/><path d="M8 9l2 2 3-4" stroke="#fff" fill="none"/></svg></div>
  <p class="cap" style="left:171px;top:53px">Introduce a search policy</p>
  <div class="tile t" style="left:242px;top:45px"><svg width="16" height="14" viewBox="0 0 16 14"><circle cx="8" cy="3" r="2.3" fill="none" stroke="#fff"/><rect x="2" y="7" width="3" height="6" fill="none" stroke="#fff"/><rect x="6.5" y="7" width="3" height="6" fill="none" stroke="#fff"/><rect x="11" y="7" width="3" height="6" fill="none" stroke="#fff"/></svg></div>
  <p class="cap" style="left:276px;top:50px">Regular stock balance checks of all CD's</p>

  <div class="tile k" style="left:33px;top:94px"><svg width="16" height="14" viewBox="0 0 16 14"><rect x="2" y="3" width="10" height="5" rx="1" fill="#fff" transform="rotate(15 7 5)"/><path d="M6 9v4H3" stroke="#fff" fill="none"/></svg></div>
  <p class="cap" style="left:67px;top:105px">CCTV</p>
  <div class="tile t" style="left:137px;top:94px"><svg width="16" height="12" viewBox="0 0 16 12"><rect x="1" y="1" width="14" height="10" rx="1" fill="none" stroke="#fff"/><path d="M3 5h6M3 8h4" stroke="#fff" stroke-width=".8"/><circle cx="12" cy="7" r="1.8" fill="#fff"/></svg></div>
  <p class="cap" style="left:171px;top:99px">Check DBS checks are up to date</p>
  <div class="tile k" style="left:242px;top:94px"><svg width="14" height="16" viewBox="0 0 14 16"><rect x="1" y="1" width="12" height="14" rx="1" fill="none" stroke="#fff"/><path d="M4 5h6M4 8h6M4 11h6" stroke="#fff" stroke-width=".8"/></svg></div>
  <p class="cap" style="left:276px;top:99px">Regular CD training / re-reading of SOP's</p>

  <div class="tile t" style="left:33px;top:138px"><svg width="14" height="16" viewBox="0 0 14 16"><g fill="#fff"><circle cx="3" cy="3" r="1.1"/><circle cx="7" cy="3" r="1.1"/><circle cx="11" cy="3" r="1.1"/><circle cx="3" cy="7" r="1.1"/><circle cx="7" cy="7" r="1.1"/><circle cx="11" cy="7" r="1.1"/></g><path d="M6 15v-5a1 1 0 0 1 2 0v3h3v2" stroke="#fff" fill="none" stroke-width=".8"/></svg></div>
  <p class="cap" style="left:67px;top:143px">Change door codes regularly</p>
  <div class="tile k" style="left:137px;top:138px"><svg width="16" height="12" viewBox="0 0 16 12"><g fill="none" stroke="#fff" stroke-width=".8"><circle cx="4" cy="3.5" r="2"/><circle cx="12" cy="3.5" r="2"/><path d="M1 11a3 3 0 0 1 6 0M9 11a3 3 0 0 1 6 0"/></g></svg></div>
  <p class="cap" style="left:171px;top:139px">Too much responsibility given to junior unregulated staff !</p>
  <div class="tile t" style="left:242px;top:138px"><svg width="16" height="16" viewBox="0 0 16 16"><g fill="none" stroke="#fff" stroke-width=".8"><path d="M8 14a6 6 0 1 1 6-6"/><path d="M8 11a3 3 0 1 1 3-3"/><path d="M10 10l4 5"/></g></svg></div>
  <p class="cap" style="left:276px;top:143px">Swipe card security – deny access/monitor</p>
  <div class="slide-foot"><span class="dot"></span><span class="legal">©2023. Kestrel Ward Consulting Ltd</span><span class="line"></span><span class="page">8</span></div>
</section>

<section class="slide col-1 row-4 invest">
  <h2 class="slide-title">Internal Investigations</h2>
  <svg class="title-rule" viewBox="0 0 42 3"><circle cx="1.2" cy="1.5" r="1.1" fill="#1fb3aa"/><circle cx="4.2" cy="1.5" r="1.1" fill="#1fb3aa"/><circle cx="7.2" cy="1.5" r="1.1" fill="#1fb3aa"/><rect x="9.5" y=".6" width="32" height="1.8" fill="#1fb3aa"/></svg>
  <div class="brand-tag"><span class="dot"></span><span class="name">Kestrel Ward<br>Consulting</span></div>
  <svg class="abs" style="left:0;top:0" width="357" height="201" viewBox="0 0 357 201">
    <g stroke="#1d2626" stroke-width=".7" fill="none"><path d="M154,84 L163,80"/><path d="M197,80 L205,84"/><path d="M127,108 L123,117"/><path d="M233,108 L237,117"/><path d="M122,152 L123,160"/><path d="M240,152 L238,160"/></g>
  </svg>
  <div class="node" style="left:165px;top:62px"><svg width="12" height="12" viewBox="0 0 12 12"><circle cx="6" cy="3.5" r="2.3" fill="#fff"/><path d="M1.5 11a4.5 4.5 0 0 1 9 0Z" fill="#fff"/></svg></div>
  <div class="node" style="left:124px;top:79px"><svg width="14" height="12" viewBox="0 0 14 12"><g fill="#fff"><circle cx="7" cy="3" r="1.8"/><circle cx="3" cy="5" r="1.4"/><circle cx="11" cy="5" r="1.4"/><path d="M4 11a3 3 0 0 1 6 0Z"/></g></svg></div>
  <div class="node" style="left:206px;top:79px"><svg width="14" height="12" viewBox="0 0 14 12"><g fill="#fff"><circle cx="5" cy="3" r="2.2"/><path d="M1 11a4 4 0 0 1 8 0Z"/></g><circle cx="11" cy="8" r="2.2" fill="none" stroke="#fff" stroke-width=".8"/></svg></div>
  <div class="node" style="left:106px;top:118px"><svg width="14" height="12" viewBox="0 0 14 12"><g fill="none" stroke="#fff" stroke-width=".8"><circle cx="7" cy="4" r="3"/><path d="M7 2.5V4h1.5"/><path d="M1 6c0 3 2 5 4 5M13 6c0 3-2 5-4 5"/></g></svg></div>
  <div class="node" style="left:224px;top:118px"><svg width="12" height="12" viewBox="0 0 12 12"><g fill="#fff"><circle cx="6" cy="3.5" r="2.3"/><path d="M1.5 11a4.5 4.5 0 0 1 9 0Z"/></g></svg></div>
  <p class="cap" style="left:152px;top:44px;text-align:center;width:56px">Senior member<br>of staff</p>
  <p class="cap" style="left:72px;top:87px">Experienced</p>
  <p class="cap" style="left:243px;top:80px">Not socially<br>acquainted with<br>the suspect</p>
  <p class="cap" style="left:33px;top:124px;text-align:right;width:68px">Someone with<br>time to &nbsp;conduct<br>the investigation</p>
  <p class="cap" style="left:262px;top:124px">Someone<br>easily<br>contactable</p>
  <p class="abs who">Who<br>Should<br>Investigate?</p>
  <div class="slide-foot"><span class="dot"></span><span class="legal">©2023. Kestrel Ward Consulting Ltd</span><span class="line"></span><span class="page">9</span></div>
</section>

<section class="slide col-2 row-4 speak">
  <h2 class="slide-title">What is speaking up?</h2>
  <svg class="title-rule" viewBox="0 0 42 3"><circle cx="1.2" cy="1.5" r="1.1" fill="#1fb3aa"/><circle cx="4.2" cy="1.5" r="1.1" fill="#1fb3aa"/><circle cx="7.2" cy="1.5" r="1.1" fill="#1fb3aa"/><rect x="9.5" y=".6" width="32" height="1.8" fill="#1fb3aa"/></svg>
  <div class="brand-tag"><span class="dot"></span><span class="name">Kestrel Ward<br>Consulting</span></div>
  <div class="photo" role="img" aria-label="Illustration of a teal megaphone with the words speak up" style="left:32px;top:63px;width:103px;height:95px;background:linear-gradient(135deg,#e6f7f6,#bfeae6)"></div>
  <ul class="bullets">
    <li>When things go wrong, we need to make sure that lessons are learnt and things are improved.</li>
    <li>If we think something might go wrong, it's important that we all feel able to speak up so that potential harm is prevented.</li>
    <li>Even when things are good, but could be even better, we should feel able to say something and should expect that our suggestion is listened to and used as an opportunity for improvement.</li>
  </ul>
  <div class="slide-foot"><span class="dot"></span><span class="legal">©2023. Kestrel Ward Consulting Ltd</span><span class="line"></span><span class="page">9</span></div>
</section>

<section class="slide col-3 row-4 thanks">
  <div class="abs ring"></div>
  <div class="abs brand">Kestrel Ward<span>Consulting</span></div>
  <h2>Thank You</h2>
  <div class="contact" style="top:118px"><svg width="8" height="8" viewBox="0 0 8 8"><path d="M1.5 1 3 .8 3.8 2.6 2.8 3.4A4.5 4.5 0 0 0 4.6 5.2L5.4 4.2 7.2 5 7 6.5C3.5 7 1 4.5 1.5 1Z" fill="#1fb3aa"/></svg><span class="bar"></span><span>+18 2767 9470 1808<br>+18 2767 9470 1808</span></div>
  <div class="contact" style="top:141px"><svg width="8" height="8" viewBox="0 0 8 8"><path d="M.5 3.5 7.5.5 4.5 7.5 3.8 4.2Z" fill="#1fb3aa"/></svg><span class="bar"></span><span>www.websitename.com<br>urname@email.com</span></div>
  <div class="contact" style="top:160px"><svg width="8" height="8" viewBox="0 0 8 8"><path d="M4 .8 7.5 4H6.5V7.5H4.7V5.5H3.3V7.5H1.5V4H.5Z" fill="#1fb3aa"/></svg><span class="bar"></span><span>1234 Street name, town/city,<br>state/country, post/zip 012345.</span></div>
  <svg class="abs strip" viewBox="0 0 357 10" preserveAspectRatio="none"><polygon points="130,0 357,0 357,10 116,10" fill="#1fb3aa"/><polygon points="128,6 357,6 357,10 120,10" fill="#169b93"/></svg>
</section>

</body>
</html>
```